Classy, Elegant, Simple Business Card Design

Looking to have a classy, simple, and elegant design. Want a top notch designed business card. I really like the look of the new brivo credit card. I also like the design I attached. I am trying to reach 21-29 year old females for booking us for there wedding or event. We offer Disc Jockey Service, Photo Booth Rentals, and Uplighting .

Target Market(s)

21-28 year old females

Contact Information for Business Card

Has to have logo, website, email, and phone number

Font styles to use
Other font styles liked:
• open to font choice, modern, clean
Designer to choose
33a6d7
0791cd
0555a3
ffffff

Requirements
Must have
• Has to have logo, website, email, and phone number
Nice to have
• I really like the design of the new brivo credit card. I also included my logo and some designs I like
Should not have
• clutter or too much info

```html
<!DOCTYPE html>
<html lang="en">
<head>
<meta charset="utf-8">
<title>Tidecrest Business Card</title>
<link rel="stylesheet" href="https://fonts.googleapis.com/css2?family=Roboto:wght@500&display=swap">
<style>
  :root {
    --backdrop: #0071b2;
    --card: #f2f2f2;
    --card-light: #ffffff;
    --brand: #0791cd;
    --text-grey: #8e8e8e;
    --icon: #3b3570;
  }
  html, body {
    margin: 0;
    width: 1200px;
    height: 1009px;
    overflow: hidden;
    background: var(--backdrop);
  }
  .card {
    position: absolute;
    left: 70px;
    top: 200px;
    width: 1048px;
    height: 598px;
    border-radius: 62px;
    background: var(--card);
    overflow: hidden;
  }
  .card__rays {
    position: absolute;
    inset: 0;
  }
  .brand {
    position: absolute;
    right: 112px;
    top: 84px;
    width: 200px;
    display: flex;
    flex-direction: column;
    align-items: center;
    gap: 18px;
  }
  .brand__mark {
    width: 74px;
    height: 74px;
    border-radius: 50%;
    background: var(--brand);
  }
  .brand__name {
    font-family: "Roboto", sans-serif;
    font-weight: 500;
    font-size: 28px;
    letter-spacing: 1px;
    color: var(--brand);
  }
  .contact {
    position: absolute;
    left: 48px;
    top: 452px;
    margin: 0;
    padding: 0;
    list-style: none;
  }
  .contact__item {
    display: flex;
    align-items: center;
    height: 40px;
    font-family: "Roboto", sans-serif;
    font-weight: 500;
    font-size: 26px;
    color: var(--text-grey);
  }
  .contact__icon {
    width: 26px;
    height: 26px;
    margin-right: 11px;
    flex: none;
  }
</style>
</head>
<body>
  <div class="card">
    <svg class="card__rays" width="1048" height="598" viewBox="0 0 1048 598" aria-hidden="true">
      <defs>
        <linearGradient id="ray" x1="1" y1="0" x2="0" y2="1">
          <stop offset="0" stop-color="#ffffff" stop-opacity="1"/>
          <stop offset="1" stop-color="#ffffff" stop-opacity="0.2"/>
        </linearGradient>
      </defs>
      <polygon points="930,0 0,225 0,320 1048,0" fill="url(#ray)" opacity="0.6"/>
      <polygon points="1048,0 0,320 0,598 620,598 1048,130" fill="url(#ray)" opacity="0.9"/>
      <polygon points="1048,130 620,598 750,598 1048,125" fill="#ffffff" opacity="0.5"/>
    </svg>

    <div class="brand">
      <div class="brand__mark"></div>
      <div class="brand__name">TIDECREST</div>
    </div>

    <ul class="contact">
      <li class="contact__item">
        <svg class="contact__icon" viewBox="0 0 24 24" fill="none" stroke="var(--icon)" stroke-width="1.4">
          <circle cx="12" cy="12" r="10"/>
          <ellipse cx="12" cy="12" rx="4.5" ry="10"/>
          <line x1="2" y1="12" x2="22" y2="12"/>
          <path d="M4 7h16M4 17h16"/>
        </svg>
        www.tidecrest.com
      </li>
      <li class="contact__item">
        <svg class="contact__icon" viewBox="0 0 24 24" fill="none" stroke="var(--icon)" stroke-width="1.4">
          <rect x="2" y="5" width="20" height="14" rx="1.5"/>
          <path d="M2.5 5.5 12 13l9.5-7.5"/>
        </svg>
        hello@tidecrest.com
      </li>
      <li class="contact__item">
        <svg class="contact__icon" viewBox="0 0 24 24" fill="none" stroke="var(--icon)" stroke-width="1.4">
          <path d="M6 3l3 4-2 2c1 2.5 3.5 5 6 6l2-2 4 3-2 3C10 19 5 14 3 6z"/>
          <path d="M14 6a4 4 0 0 1 4 4M14 2.5a7.5 7.5 0 0 1 7.5 7.5"/>
        </svg>
        0000 00000
      </li>
    </ul>
  </div>
</body>
</html>
```